Rolla Maki Hospitality Brochure for Industry leaders within the catering space

We need a brochure created for a Sushi franchise called Rolla Maki. The brochure will be 6 pages including the front and back pages.
Background white.
Content to be displayed as written.
Images to be creatively placed throughout document.

refer to www.rollamaki.com.au

refer to document notes

Target Market(s)

hospitality catering companies
remote locations

Font styles to use
Other font styles liked:
• some wood finish is ok.

Colors
ec1f27
ffffff

Requirements
Must have
• stylish
A4
Portrait
Nice to have
• background photos included
health
well being

```html
<!DOCTYPE html>
<html lang="en">
<head>
<meta charset="utf-8">
<title>Rolla Maki – Brochure</title>
<link href="https://fonts.googleapis.com/css2?family=Oswald:wght@500&family=Roboto+Condensed:ital,wght@0,400;0,700;1,400&display=swap" rel="stylesheet">
<style>
  :root {
    --red: #a81d25;
    --red-bright: #c2222b;
    --green: #72a84c;
    --ink: #2b2b2b;
    --paper: #ffffff;
    --backdrop: #ebe9e5;
  }
  * { box-sizing: border-box; margin: 0; padding: 0; }
  html, body { width: 1200px; height: 900px; overflow: hidden; background: var(--backdrop); }
  body { position: relative; font-family: "Roboto Condensed", "Arial Narrow", sans-serif; color: var(--ink); }

  .page {
    position: absolute; top: 199px; width: 355px; height: 502px;
    background: var(--paper); overflow: hidden;
    box-shadow: 0 6px 18px rgba(0,0,0,.14);
  }
  .cover { left: 45px; }
  .spread { position: absolute; top: 199px; left: 445px; width: 710px; height: 502px; box-shadow: 0 6px 18px rgba(0,0,0,.14); }
  .spread .page { top: 0; box-shadow: none; }
  .inner-left { left: 0; }
  .inner-right { left: 355px; }
  .spread .gutter { position: absolute; left: 354px; top: 0; width: 2px; height: 502px; background: linear-gradient(90deg, rgba(0,0,0,.12), rgba(0,0,0,0)); z-index: 5; }

  .page-shapes { position: absolute; inset: 0; width: 355px; height: 502px; }

  /* Cover */
  .brand { position: absolute; top: 62px; right: 52px; display: flex; align-items: center; gap: 10px; }
  .brand-dot { width: 30px; height: 30px; border-radius: 50%; background: var(--green); }
  .brand-name { font-family: "Oswald", "Arial Narrow", sans-serif; font-weight: 500; font-size: 40px; color: var(--red); letter-spacing: 1px; line-height: 1; }
  .cover-tagline {
    position: absolute; top: 175px; left: 22px; right: 0;
    border: 1.5px solid var(--green); border-right: none; padding: 8px 14px;
  }
  .cover-tagline h1 { font-family: "Oswald", "Arial Narrow", sans-serif; font-weight: 500; font-size: 23px; color: var(--red); letter-spacing: .3px; }
  .cover-sub { position: absolute; top: 232px; left: 30px; font-size: 13px; font-weight: 700; color: var(--ink); }
  .cover-photo {
    position: absolute; left: 0; bottom: 8px; width: 355px; height: 205px;
    background: linear-gradient(135deg, #f08a4b 0%, #f4efe6 30%, #e9653a 52%, #2f3a2a 70%, #f6d9b6 100%);
  }
  .cover-edge { position: absolute; left: 0; bottom: 0; width: 355px; height: 8px; background: var(--green); }

  /* Inner left */
  .circle-photo {
    position: absolute; left: 172px; top: 38px; width: 210px; height: 210px; border-radius: 50%;
    border: 4px solid var(--paper);
    background: radial-gradient(circle at 45% 50%, #b9825a 0%, #8a5a3c 45%, #d8583a 75%, #3c3231 100%);
  }
  .bubble {
    position: absolute; left: 52px; top: 62px; width: 118px; height: 112px;
    background: var(--green); border-radius: 50% 50% 6px 50%;
    display: flex; align-items: center; justify-content: center; text-align: center;
    color: var(--paper); font-size: 10px; letter-spacing: 1.2px; text-transform: uppercase; line-height: 1.45; padding: 10px;
  }
  .intro-heading {
    position: absolute; left: 30px; top: 238px; width: 270px;
    font-family: "Oswald", "Arial Narrow", sans-serif; font-weight: 500; font-size: 19px; line-height: 1.15; color: var(--red);
  }
  .intro-rule { position: absolute; left: 30px; top: 290px; width: 40px; height: 1.5px; background: var(--red); }
  .intro-body { position: absolute; left: 30px; top: 300px; width: 290px; font-size: 8.4px; line-height: 1.42; }
  .intro-body p + p { margin-top: 6px; }

  /* Inner right */
  .snap { position: absolute; top: 46px; width: 100px; height: 80px; border: 4px solid var(--paper); box-shadow: 0 2px 5px rgba(0,0,0,.25); }
  .snap-health { left: 22px; transform: rotate(-3deg); background: linear-gradient(135deg, #e8e3dc, #b84a3a 55%, #6f8d4a); }
  .snap-kitchen { left: 128px; top: 52px; transform: rotate(2deg); background: linear-gradient(160deg, #5a5148, #c9b592 55%, #3b3530); }
  .snap-site { left: 234px; top: 48px; transform: rotate(-2deg); background: linear-gradient(180deg, #b9c3cc 0%, #d5dbe0 45%, #5c5650 70%, #e4742c 100%); }
  .why { position: absolute; left: 30px; top: 215px; width: 300px; }
  .why-kicker { font-family: "Oswald", "Arial Narrow", sans-serif; font-weight: 500; font-size: 14px; color: var(--red); }
  .why h2 { font-family: "Oswald", "Arial Narrow", sans-serif; font-weight: 500; font-size: 17px; color: var(--red); line-height: 1.2; }
  .why-rule { width: 40px; height: 1.5px; background: var(--red); margin: 7px 0 8px; }
  .why-lead { font-size: 12px; font-weight: 700; margin-bottom: 10px; }
  .ticks { list-style: none; }
  .ticks li { position: relative; padding-left: 18px; font-size: 8.4px; line-height: 1.42; margin-bottom: 7px; }
  .ticks svg { position: absolute; left: 0; top: 1px; width: 11px; height: 11px; }
  .site-url { position: absolute; left: 0; right: 0; bottom: 7px; text-align: center; color: var(--paper); font-size: 9px; letter-spacing: 1.5px; }
</style>
</head>
<body>

<section class="page cover">
  <div class="brand">
    <span class="brand-dot"></span>
    <span class="brand-name">ROLLA MAKI</span>
  </div>
  <div class="cover-tagline"><h1>MORE CHOICE AT MEALTIMES!</h1></div>
  <p class="cover-sub">More variety at mealtimes means a happier workforce!</p>
  <div class="cover-photo" role="img" aria-label="Close-up photo of assorted sushi rolls and salmon nigiri"></div>
  <div class="cover-edge"></div>
</section>

<section class="spread">
  <div class="page inner-left">
    <svg class="page-shapes" viewBox="0 0 355 502" aria-hidden="true">
      <polygon points="0,0 355,0 355,235 0,95" fill="var(--red)"/>
      <polygon points="0,468 355,496 355,502 0,502" fill="var(--green)"/>
    </svg>
    <div class="circle-photo" role="img" aria-label="Photo of friends sharing sushi at a table, photographing the food with their phones"></div>
    <div class="bubble">Nourishing more and more Australians every year</div>
    <h2 class="intro-heading">Spice up mealtimes with an on-trend favourite.</h2>
    <div class="intro-rule"></div>
    <div class="intro-body">
      <p>We understand how important mealtimes are after such long, hard shifts. Away from home and family, food becomes one of the most appreciated creature comforts for remote workers. So why not provide them with greater variety at a time they need it most, whilst unwinding and socialising?</p>
      <p>Refueling the body with diverse nutrient rich foods is essential in keeping them safe and mentally supported, protecting them from illness and strengthening overall productivity.</p>
      <p>Rolla Maki ticks all the boxes! It's a popular nutritional must-have your workforce will love at any time of the day and with a foolproof franchising system designed for success, the benefits to all are hard to ignore.</p>
    </div>
  </div>

  <div class="page inner-right">
    <svg class="page-shapes" viewBox="0 0 355 502" aria-hidden="true">
      <polygon points="0,0 355,0 355,170 0,200" fill="var(--red)"/>
      <polygon points="0,488 355,470 355,502 0,502" fill="var(--green)"/>
    </svg>
    <div class="snap snap-health" role="img" aria-label="Photo of a heart-shaped bowl of fresh produce beside a stethoscope"></div>
    <div class="snap snap-kitchen" role="img" aria-label="Photo of a sushi kiosk counter"></div>
    <div class="snap snap-site" role="img" aria-label="Photo of workers in high-visibility vests at a remote mine site"></div>

    <div class="why">
      <p class="why-kicker">Why sushi?</p>
      <h2>A winning choice on taste and on trend.</h2>
      <div class="why-rule"></div>
      <p class="why-lead">On trend and loved by more Australians every year!</p>
      <ul class="ticks">
        <li><svg viewBox="0 0 12 12"><circle cx="6" cy="6" r="5.3" fill="none" stroke="var(--green)" stroke-width="1.2"/><path d="M3.4 6.2 5.3 8 8.7 4.3" fill="none" stroke="var(--green)" stroke-width="1.4"/></svg>Sushi is hugely popular with over 8.5 million Australians ranking it as a favourite meal. According to leading market research organization Kestrel Research, its popularity continues to rise year on year.</li>
        <li><svg viewBox="0 0 12 12"><circle cx="6" cy="6" r="5.3" fill="none" stroke="var(--green)" stroke-width="1.2"/><path d="M3.4 6.2 5.3 8 8.7 4.3" fill="none" stroke="var(--green)" stroke-width="1.4"/></svg>It offers a powerhouse of nutrition by containing a variety of fish which are full of essential fatty acids for heart and cholesterol health, arterial strength, brain function and importantly to help as a mood enhancer to alleviate depression (OR to support mental wellbeing).</li>
        <li><svg viewBox="0 0 12 12"><circle cx="6" cy="6" r="5.3" fill="none" stroke="var(--green)" stroke-width="1.2"/><path d="M3.4 6.2 5.3 8 8.7 4.3" fill="none" stroke="var(--green)" stroke-width="1.4"/></svg>With its fresh colours and creative presentation, sushi celebrates the notion that when you "eat with your eyes" the food becomes more appetizing and enjoyable; a sensory experience that few foods can match.</li>
        <li><svg viewBox="0 0 12 12"><circle cx="6" cy="6" r="5.3" fill="none" stroke="var(--green)" stroke-width="1.2"/><path d="M3.4 6.2 5.3 8 8.7 4.3" fill="none" stroke="var(--green)" stroke-width="1.4"/></svg>Sushi is a healthy and convenient food choice that workers can grab and go.</li>
      </ul>
    </div>
    <p class="site-url">www.rollamaki.com.au</p>
  </div>
  <div class="gutter"></div>
</section>

</body>
</html>
```